Create Lanternfield HR Business Cards.

Create Business Cards for Lanternfield HR. 2 sided and Would like the back to have the logo.

Info for Business Card:
Address: 4827 Millbrook Ave Suite 230 Cleveland, Ohio 44987
Office Number: 216-555-0143
Mobile: 216-555-0192

Website: www.lanternfieldhr.example

Target Market(s)

Small to medium size businesses

Industry/Entity Type

Human Resources

Contact Information for Business Card

Company logo and information

Font styles to use
Serif
Sans Serif

Requirements
Must have
• Info for Business Card: Address: 4827 Millbrook Ave Suite 230 Cleveland, Ohio 44987 Office Number: 216-555-0143 Mobile: 216-555-0192 Website: www.lanternfieldhr.example

```html
<!DOCTYPE html>
<html lang="en">
<head>
<meta charset="utf-8">
<title>Lanternfield HR Business Cards</title>
<link href="https://fonts.googleapis.com/css2?family=Montserrat:wght@600;800&family=Lato:wght@400;700&display=swap" rel="stylesheet">
<style>
  :root {
    --navy: #262064;
    --navy-deep: #1f1a55;
    --orange: #f7860f;
    --white: #ffffff;
    --muted: #d9d7ee;
    --backdrop: #2a2a2c;
  }
  * { margin: 0; padding: 0; box-sizing: border-box; }
  html, body { width: 1200px; height: 952px; overflow: hidden; background: var(--backdrop); }
  .sheet {
    width: 1200px; height: 952px;
    display: flex; flex-direction: column; align-items: center; justify-content: center; gap: 56px;
  }
  .card {
    position: relative; width: 700px; height: 400px;
    background: var(--navy); overflow: hidden;
    box-shadow: 0 16px 40px rgba(0,0,0,.45);
  }
  /* front */
  .accent-top { position: absolute; left: 0; top: 0; width: 14px; height: 150px; background: var(--orange); }
  .accent-bottom { position: absolute; right: 0; bottom: 0; width: 14px; height: 150px; background: var(--orange); }
  .brand {
    position: absolute; left: 70px; top: 120px; width: 240px;
    display: flex; align-items: center; gap: 12px;
  }
  .brand-dot { width: 30px; height: 30px; border-radius: 50%; background: var(--orange); flex: none; }
  .brand-name {
    font-family: "Montserrat", sans-serif; font-weight: 800; font-size: 27px;
    line-height: 1.1; color: var(--white); letter-spacing: .5px;
  }
  .divider { position: absolute; left: 340px; top: 90px; width: 1px; height: 170px; background: rgba(255,255,255,.28); }
  .contact { position: absolute; left: 372px; top: 108px; }
  .person {
    font-family: "Montserrat", sans-serif; font-weight: 600; font-size: 22px;
    color: var(--white); letter-spacing: .5px;
  }
  .person .surname { color: var(--orange); font-weight: 800; }
  .role { font-family: "Lato", sans-serif; font-size: 16px; color: var(--muted); margin: 4px 0 18px; }
  .line {
    display: flex; align-items: center; gap: 10px;
    font-family: "Lato", sans-serif; font-size: 16px; color: var(--white); margin-bottom: 8px;
  }
  .line svg { width: 16px; height: 16px; flex: none; }
  .address {
    position: absolute; left: 70px; bottom: 46px;
    font-family: "Lato", sans-serif; font-size: 15px; color: var(--muted); letter-spacing: .2px;
  }
  /* back */
  .back-band { position: absolute; left: 0; right: 0; bottom: 0; height: 16px; background: var(--orange); }
  .back-name {
    position: absolute; left: 70px; bottom: 62px;
    font-family: "Montserrat", sans-serif; font-weight: 800; font-size: 46px;
    color: var(--white); letter-spacing: 1.5px; text-transform: uppercase;
  }
</style>
</head>
<body>
<main class="sheet">
  <section class="card card-front" aria-label="Business card front">
    <span class="accent-top"></span>
    <span class="accent-bottom"></span>
    <div class="brand">
      <span class="brand-dot"></span>
      <span class="brand-name">Lanternfield HR</span>
    </div>
    <span class="divider"></span>
    <div class="contact">
      <p class="person">DANIEL M. <span class="surname">HARWICK</span></p>
      <p class="role">Managing Director</p>
      <p class="line">
        <svg viewBox="0 0 16 16"><rect x="2" y="3" width="12" height="10" rx="1.5" fill="none" stroke="#f7860f" stroke-width="1.6"/><rect x="5" y="6" width="6" height="2" fill="#f7860f"/></svg>
        216-555-0143
      </p>
      <p class="line">
        <svg viewBox="0 0 16 16"><path d="M4 1.5h3l1 3.5-2 1.3a8 8 0 0 0 3.7 3.7L11 8l3.5 1v3c0 1-.8 1.8-1.8 1.8A11.5 11.5 0 0 1 2.2 3.3c0-1 .8-1.8 1.8-1.8z" fill="#f7860f"/></svg>
        216-555-0192
      </p>
      <p class="line">
        <svg viewBox="0 0 16 16"><circle cx="8" cy="8" r="6.2" fill="none" stroke="#f7860f" stroke-width="1.5"/><ellipse cx="8" cy="8" rx="2.6" ry="6.2" fill="none" stroke="#f7860f" stroke-width="1.2"/><line x1="1.8" y1="8" x2="14.2" y2="8" stroke="#f7860f" stroke-width="1.2"/></svg>
        www.lanternfieldhr.example
      </p>
    </div>
    <p class="address">4827 Millbrook Ave Suite 230 Cleveland, Ohio 44987</p>
  </section>

  <section class="card card-back" aria-label="Business card back">
    <p class="back-name">Lanternfield HR</p>
    <span class="back-band"></span>
  </section>
</main>
</body>
</html>
```